Maple Syrup Bottle (front) Label design

I need label design for a 16fl OZ rectangular bottle of maple syrup with the usable dimensions of: Front: 4" x 2" and the back area for "ingredient specifications" of: 6" x 2". The maple syrup product comes from our own farm and is a quality product. The technical name/class of the syrup is: Grade A / AMBER
Updates

I can’t seem to find a way to upload a photo of the maple syrup bottle, but the front dimensions are clearly written on bottle description. Again: 4.5” by 2.25”

I have tried to upload the photo of the maple syrup bottle several times, and it seems (from my side) that it is successful. But I can never find it and the artists cannot find it either. Not sure what to do.

I have tried several times to add a photo of maple bottle, but it never shows up

This seems to be a futile exercise

I would like to post some images of the actual quill Hollow (not the one on Fendix, though!
But I can’t get back to the page that allows that to happen. Please advise!

Somebody PLEASE ask PW management to make it possible for me to upload more images! The "add photos" etc. just disappears from anywhere.

Target Market(s)

High-end food stores

Industry/Entity Type

Maple syrup retail industry

Other font styles liked:
• I don't know, and welcome suggestions

Colors

Designer to choose colors to be used in the design.

Requirements
Must have
• Name of Farm: Quill Hollow Maple
Nice to have
• The label can be "minimalist" and elegant. There is already a Maple leaf glass relief on the top of front of the bottle.
Should not have
• and NOT include farm buildings with steam coming out the chimney, etc.

```html
<!DOCTYPE html>
<html lang="en">
<head>
<meta charset="utf-8">
<title>Quill Hollow Maple – Maple Syrup Front Label</title>
<link rel="stylesheet" href="https://fonts.googleapis.com/css2?family=Bagel+Fat+One&family=Archivo:wdth,wght@125,800&family=Figtree:wght@400&family=Rubik:wght@500&display=swap">
<style>
  :root {
    --page: #f5f5f7;
    --label: #f9e1d7;
    --red: #ec1c3d;
    --white: #ffffff;
  }
  * { box-sizing: border-box; margin: 0; padding: 0; }
  html, body {
    width: 1200px;
    height: 966px;
    overflow: hidden;
    background: var(--page);
  }
  .label {
    position: absolute;
    left: 380px;
    top: 43px;
    width: 440px;
    height: 880px;
    background: var(--label);
    color: var(--red);
  }
  .brand-mark {
    position: absolute;
    left: 110px;
    top: 67px;
    width: 220px;
    height: 220px;
    border: 2px solid var(--red);
    border-radius: 50%;
    display: flex;
    align-items: center;
    justify-content: center;
    text-align: center;
  }
  .brand-name {
    font-family: "Archivo", sans-serif;
    font-stretch: 125%;
    font-weight: 800;
    font-size: 22px;
    line-height: 1.15;
    letter-spacing: 0.04em;
    text-transform: uppercase;
    color: var(--red);
  }
  .drip {
    position: absolute;
    left: 0;
    width: 440px;
  }
  .drip-upper { top: 286px; height: 166px; }
  .drip-lower { top: 600px; height: 84px; }
  .product-title {
    position: absolute;
    top: 455px;
    left: 0;
    width: 440px;
    text-align: center;
    font-family: "Bagel Fat One", sans-serif;
    font-weight: 400;
    font-size: 66px;
    line-height: 62px;
    letter-spacing: 0.01em;
    color: var(--red);
  }
  .grade {
    position: absolute;
    left: 60px;
    top: 718px;
    width: 320px;
    height: 42px;
    border-top: 2px solid var(--red);
    border-bottom: 2px solid var(--red);
    display: flex;
    align-items: center;
    justify-content: center;
    font-family: "Archivo", sans-serif;
    font-stretch: 125%;
    font-weight: 800;
    font-size: 18px;
    letter-spacing: 0.03em;
  }
  .claims {
    position: absolute;
    top: 771px;
    left: 0;
    width: 440px;
    text-align: center;
    font-family: "Figtree", sans-serif;
    font-size: 17px;
    letter-spacing: 0.01em;
  }
  .net-weight {
    position: absolute;
    left: 16px;
    top: 820px;
    width: 408px;
    height: 43px;
    background: var(--red);
    color: var(--white);
    display: flex;
    align-items: center;
    justify-content: center;
    font-family: "Rubik", sans-serif;
    font-weight: 500;
    font-size: 18px;
    letter-spacing: 0.12em;
  }
</style>
</head>
<body>
  <main class="label">
    <div class="brand-mark">
      <p class="brand-name">Quill Hollow<br>Maple</p>
    </div>

    <svg class="drip drip-upper" viewBox="0 0 440 166" aria-hidden="true">
      <path d="M214 0 Q220 6 220 18 L220 166" fill="none" stroke="var(--red)" stroke-width="2"/>
      <path d="M226 0 Q220 6 220 18" fill="none" stroke="var(--red)" stroke-width="2"/>
    </svg>

    <h1 class="product-title">MAPLE<br>SYRUP</h1>

    <svg class="drip drip-lower" viewBox="0 0 440 84" aria-hidden="true">
      <line x1="220" y1="0" x2="220" y2="66" stroke="var(--red)" stroke-width="2"/>
      <path d="M220 64 Q225 74 225 78 A5 5 0 0 1 215 78 Q215 74 220 64 Z" fill="var(--red)"/>
    </svg>

    <p class="grade">GRADE A / AMBER</p>
    <p class="claims">All Natural | No Additives | Gluten Free</p>
    <p class="net-weight">Net. Wt. 16Fl Oz</p>
  </main>
</body>
</html>
```